I'm an electrician and the name of my company is called Brisk 'N' Bright Electrical. I require a professional business card that speaks to my clients, I also need it to be innovative and modern. We do maintenance & service work for domestic and commercial premises.

Industry/Entity Type

Electrical

Contact Information for Business Card

Must have the name of my company Brisk 'N' Bright Electrical, my name Darren Kolovos and my contact details 0427 381 592 and company email address Brisknbrightelectrical@mailvane.com and/or website Brisknbrightelectrical.com.au

Logo Text

Brisk 'N' Bright Electrical (If possible)

Colors
33a6d7
0592cd
3176b5

```html
<!DOCTYPE html>
<html lang="en">
<head>
<meta charset="utf-8">
<title>Brisk 'N' Bright Electrical — Business Card</title>
<link rel="stylesheet" href="https://fonts.googleapis.com/css2?family=Montserrat:wght@300;400;600;700&display=swap">
<style>
  :root {
    --backdrop: #1f6398;
    --card: #ffffff;
    --brand: #33a6d7;
    --brand-deep: #3176b5;
    --ink-soft: #6f6f6f;
    --rule: #c9c9c9;
  }
  * { box-sizing: border-box; margin: 0; padding: 0; }
  html, body {
    width: 1189px;
    height: 1200px;
    overflow: hidden;
    background: var(--backdrop);
    font-family: "Montserrat", sans-serif;
  }
  .canvas {
    position: relative;
    width: 1189px;
    height: 1200px;
  }
  .card {
    position: absolute;
    left: 261px;
    width: 668px;
    height: 382px;
    background: var(--card);
    border-radius: 22px;
  }
  .card--front { top: 170px; }
  .card--back { top: 648px; }

  .wordmark {
    position: absolute;
    left: 0;
    right: 0;
    text-align: center;
    color: var(--brand);
    font-weight: 700;
    line-height: 1;
  }
  .wordmark__name {
    display: block;
    font-size: 24px;
    letter-spacing: 0.5px;
  }
  .wordmark__trade {
    display: block;
    font-size: 17px;
    letter-spacing: 0.6px;
    margin-top: 14px;
  }
  .card--front .wordmark { top: 118px; }
  .card--back .wordmark { top: 148px; }

  .identity {
    position: absolute;
    right: calc(668px - 276px);
    top: 246px;
    text-align: right;
  }
  .identity__name {
    font-size: 25px;
    font-weight: 600;
    color: var(--brand);
    line-height: 1.1;
    white-space: nowrap;
  }
  .identity__role {
    font-size: 15px;
    font-weight: 400;
    color: var(--ink-soft);
    margin-top: 6px;
  }
  .divider {
    position: absolute;
    left: 294px;
    top: 248px;
    width: 2px;
    height: 51px;
    background: var(--rule);
  }
  .contact {
    position: absolute;
    left: 316px;
    top: 244px;
    list-style: none;
  }
  .contact__item {
    display: flex;
    align-items: center;
    height: 20px;
    font-size: 15.5px;
    font-weight: 300;
    color: var(--ink-soft);
    white-space: nowrap;
  }
  .contact__icon {
    width: 11px;
    height: 11px;
    margin-right: 8px;
    fill: var(--brand);
    flex: none;
  }
</style>
</head>
<body>
<main class="canvas">
  <section class="card card--front" aria-label="Business card front">
    <div class="wordmark">
      <span class="wordmark__name">BRISK 'N' BRIGHT</span>
      <span class="wordmark__trade">ELECTRICAL</span>
    </div>

    <div class="identity">
      <p class="identity__name">Darren Kolovos</p>
      <p class="identity__role">Electrician</p>
    </div>

    <span class="divider"></span>

    <ul class="contact">
      <li class="contact__item">
        <svg class="contact__icon" viewBox="0 0 24 24" aria-hidden="true"><path d="M6.6 10.8a15.1 15.1 0 0 0 6.6 6.6l2.2-2.2c.3-.3.7-.4 1-.2 1.1.4 2.3.6 3.6.6.6 0 1 .4 1 1V20c0 .6-.4 1-1 1A17 17 0 0 1 3 4c0-.6.4-1 1-1h3.5c.6 0 1 .4 1 1 0 1.3.2 2.5.6 3.6.1.3 0 .7-.2 1z"/></svg>
        0427 381 592
      </li>
      <li class="contact__item">
        <svg class="contact__icon" viewBox="0 0 24 24" aria-hidden="true"><path d="M12 2a10 10 0 1 0 5 18.7l-1-1.7A8 8 0 1 1 20 12v1.2c0 1-.7 1.8-1.6 1.8s-1.6-.8-1.6-1.8V7.5h-1.8v.9A5 5 0 1 0 16 15.7a3.4 3.4 0 0 0 2.4 1.1c1.9 0 3.6-1.5 3.6-3.6V12A10 10 0 0 0 12 2zm0 13.2a3.2 3.2 0 1 1 0-6.4 3.2 3.2 0 0 1 0 6.4z"/></svg>
        Brisknbrightelectrical@mailvane.com
      </li>
      <li class="contact__item">
        <svg class="contact__icon" viewBox="0 0 24 24" aria-hidden="true"><path d="M12 2a10 10 0 1 0 0 20 10 10 0 0 0 0-20zm6.9 6h-3a15.6 15.6 0 0 0-1.4-3.6A8 8 0 0 1 18.9 8zM12 4c.8 1.2 1.5 2.5 1.9 4h-3.8c.4-1.5 1.1-2.8 1.9-4zM4.3 14a8.2 8.2 0 0 1 0-4h3.4a16.5 16.5 0 0 0 0 4zm.8 2h3a15.6 15.6 0 0 0 1.4 3.6A8 8 0 0 1 5.1 16zm3-8h-3a8 8 0 0 1 4.4-3.6C8.9 5.5 8.4 6.7 8.1 8zM12 20c-.8-1.2-1.5-2.5-1.9-4h3.8c-.4 1.5-1.1 2.8-1.9 4zm2.3-6H9.7a14.7 14.7 0 0 1 0-4h4.6a14.7 14.7 0 0 1 0 4zm.2 5.6c.6-1.1 1.1-2.3 1.4-3.6h3a8 8 0 0 1-4.4 3.6zm1.8-5.6a16.5 16.5 0 0 0 0-4h3.4a8.2 8.2 0 0 1 0 4z"/></svg>
        Brisknbrightelectrical.com.au
      </li>
    </ul>
  </section>

  <section class="card card--back" aria-label="Business card back">
    <div class="wordmark">
      <span class="wordmark__name">BRISK 'N' BRIGHT</span>
      <span class="wordmark__trade">ELECTRICAL</span>
    </div>
  </section>
</main>
</body>
</html>
```